Modern Business Card For A Digital Advertising Company

I'll be print on the Tally Prints Velvet paper http://us.tallyprints-example.com/products/velvet/business-cards.html
Need's to be modern and use the color palette of the logo or gray scales. I think integrating the pixelation of the logo in to the card and having it wrap from one side to the other could be interesting. My company provides ad operations, web development, and number of other services to websites around the world. You can see my website at http://www.brightorbitads-example.com
Contact info on the card needs to have
Dana Welby
President
p.555.308.4127
dana@brightorbitads-example.com
http://www.brightorbitads-example.com
Doesn't necessarily need to be in that order
Target Market(s)
Website owners
Industry/Entity Type
Business
Look and feel
Each slider illustrates characteristics of the customer's brand and the style your logo design should communicate.

```html
<!DOCTYPE html>
<html lang="en">
<head>
<meta charset="utf-8">
<title>Dana Welby – Business Card</title>
<link href="https://fonts.googleapis.com/css2?family=Roboto+Condensed:wght@700&family=Arimo:wght@700&display=swap" rel="stylesheet">
<style>
  :root {
    --ink-green: #17603a;
    --leaf-green: #6cbf3a;
    --lime: #8cc63f;
    --pale-green: #e3efd2;
    --paler-green: #eef6e4;
    --paper: #ffffff;
    --frame: #3a3a3a;
  }
  html, body {
    margin: 0;
    padding: 0;
    width: 1200px;
    height: 736px;
    overflow: hidden;
    background: var(--paper);
  }
  .card {
    position: relative;
    width: 1200px;
    height: 736px;
    box-sizing: border-box;
    border: 2px solid var(--frame);
    background: var(--paper);
    overflow: hidden;
  }
  .card-backdrop {
    position: absolute;
    inset: 0;
    width: 100%;
    height: 100%;
  }
  .pixel-field {
    position: absolute;
    left: 0;
    right: 0;
    bottom: 0;
    height: 300px;
    clip-path: polygon(0 55%, 100% 0, 100% 100%, 0 100%);
    background: linear-gradient(160deg, var(--paler-green) 0%, var(--pale-green) 60%, var(--paler-green) 100%);
  }
  .identity {
    position: absolute;
    left: 74px;
    top: 272px;
  }
  .identity-name {
    margin: 0;
    font-family: "Roboto Condensed", "Arial Narrow", sans-serif;
    font-weight: 700;
    font-size: 84px;
    line-height: 1;
    letter-spacing: -0.5px;
    color: var(--ink-green);
  }
  .identity-title {
    margin: 6px 0 0 2px;
    font-family: "Arimo", Arial, sans-serif;
    font-weight: 700;
    font-size: 41px;
    line-height: 1.1;
    color: var(--leaf-green);
  }
  .contact {
    position: absolute;
    left: 74px;
    top: 500px;
    font-family: "Arimo", Arial, sans-serif;
    font-weight: 700;
    font-size: 29px;
    line-height: 1.25;
    color: var(--ink-green);
  }
  .contact p { margin: 0; }
  .contact-phone { margin-bottom: 30px !important; }
  .brand {
    position: absolute;
    left: 725px;
    top: 230px;
    display: flex;
    flex-direction: column;
    align-items: flex-start;
    gap: 26px;
  }
  .brand-square {
    width: 150px;
    height: 150px;
    background: var(--lime);
  }
  .brand-name {
    margin: 0;
    font-family: "Arimo", Arial, sans-serif;
    font-weight: 700;
    font-size: 50px;
    line-height: 1.1;
    color: var(--lime);
    text-transform: uppercase;
  }
</style>
</head>
<body>
  <main class="card">
    <svg class="card-backdrop" viewBox="0 0 1200 736" aria-hidden="true">
      <polygon points="0,0 200,0 290,440 0,500" fill="var(--pale-green)"/>
      <polygon points="1050,0 1200,0 1200,300 1120,320" fill="var(--pale-green)"/>
      <polygon points="1000,420 1200,380 1200,480 1030,520" fill="var(--paler-green)"/>
    </svg>

    <div class="pixel-field" role="img" aria-label="Pale green pixel squares sweeping across the lower card"></div>

    <section class="identity">
      <h1 class="identity-name">Dana Welby</h1>
      <p class="identity-title">President</p>
    </section>

    <section class="contact">
      <p class="contact-phone">p.555.308.4127</p>
      <p class="contact-email">dana@brightorbitads-example.com</p>
      <p class="contact-web">http://www.brightorbitads-example.com</p>
    </section>

    <div class="brand">
      <div class="brand-square"></div>
      <p class="brand-name">Bright Orbit<br>Ads</p>
    </div>
  </main>
</body>
</html>
```